Fjellmark Botanics - Black Face Mask Packaging Design

We require packaging design for a charcoal activated blackhead removal peel off face mask (please see attachment of competitors product).

1: We require a logo for our brand name: 'Fjellmark Botanics'

2: We require a 3d rendered image of the box with the tube

3: We require label templates for both the box and the tube

The logo design brief is as follows:

We are bringing out a range of natural beauty products. We require a logo that represents norwegian natural beauty & incorporates the Norwegian Flag.

The packaging design brief is as follows:

Please attachment: (FBGen). There is an image of a woman with a black face mask.

1:We require our packaging design to have a generic face with a face mask being pulled off/stretched (as shown in the above attachment).
However, the face mask should display a Norwegian flag. The part of the mask that is still fixed to the face should be in full pastel Norwegian flag colors. The part of the mask that has been peeled away should be faded to charcoal grey (whilst maintaining the Norwegian flag). The ratio should be around 50/50 of mask attached to mask being peeled.
The colors throughout should be soft.

2:The design should also incorporate a unisex logo.(Please see attachment: FBUnisex)

3: The design should display the wording: 'Charcoal Activated Face Mask'

4: The design should also display the tagline: 'restores your youthful glow'

5: The back of the tube should display the ingredients: Please see attached. The back should also say ISO901 & GMPC certified

Please note, the packaging design for the tube should just be black and white as the printing machine on the tube can only be white.

The box can be a variation of colors as there are no restrictions on the colors for printing onto cardboard

Target Market(s)

Beauty, Natural Beauty, Unisex

Industry/Entity Type

Product

Logo Text

Fjellmark Botanics

Requirements
Must have
• Please refer to project description
Nice to have

```html
<!DOCTYPE html>
<html lang="en">
<head>
<meta charset="utf-8">
<title>Fjellmark Botanics – Charcoal Activated Face Mask Tube Labels</title>
<link rel="stylesheet" href="https://fonts.googleapis.com/css2?family=Bodoni+Moda:ital,wght@0,400;1,400&family=Oswald:wght@200&display=swap">
<style>
  :root {
    --backdrop: #221e1f;
    --label-white: #ffffff;
    --crimp-line: #8a8a8a;
    --cap-black: #000000;
    --ink: #1a1a1a;
    --ink-soft: #b9b9b9;
    --edge-shade: #d6d6d6;
  }
  html, body {
    margin: 0;
    padding: 0;
    overflow: hidden;
  }
  .canvas {
    position: relative;
    width: 1200px;
    height: 849px;
    background: var(--backdrop);
    overflow: hidden;
  }
  .tube {
    position: absolute;
    top: 154px;
    width: 210px;
    height: 582px;
  }
  .tube--front { left: 264px; }
  .tube--back { left: 627px; }

  .tube__crimp {
    position: absolute;
    left: 0;
    top: 0;
    width: 210px;
    height: 18px;
    background:
      repeating-linear-gradient(90deg, var(--label-white) 0 2px, var(--crimp-line) 2px 3px);
  }
  .tube__body {
    position: absolute;
    left: 0;
    top: 18px;
    width: 210px;
    height: 466px;
    background: linear-gradient(90deg, var(--label-white) 0 96%, var(--edge-shade) 100%);
    clip-path: polygon(0 0, 100% 0, 97% 100%, 3% 100%);
  }
  .tube__cap {
    position: absolute;
    left: 13px;
    top: 484px;
    width: 182px;
    height: 96px;
    background: var(--cap-black);
    border: 1px solid var(--label-white);
    border-top: none;
    border-radius: 0 0 14px 14px;
    box-sizing: border-box;
  }

  .front-label {
    position: absolute;
    left: 0;
    top: 0;
    width: 210px;
    height: 466px;
    font-family: "Bodoni Moda", serif;
    color: var(--ink);
  }
  .brand-name {
    position: absolute;
    left: 33px;
    top: 123px;
    margin: 0;
    font-weight: 400;
    font-size: 29px;
    line-height: 31px;
    letter-spacing: -0.2px;
  }
  .product-name {
    position: absolute;
    left: 40px;
    top: 201px;
    margin: 0;
    font-weight: 400;
    font-size: 15px;
    line-height: 17px;
  }
  .tagline {
    position: absolute;
    left: 40px;
    top: 240px;
    margin: 0;
    font-style: italic;
    font-size: 7.5px;
    color: var(--ink-soft);
  }
  .brand-dot {
    position: absolute;
    left: 90px;
    top: 258px;
    width: 18px;
    height: 18px;
    border-radius: 50%;
    border: 1px solid var(--ink-soft);
    box-sizing: border-box;
  }
  .volume {
    position: absolute;
    left: 0;
    width: 198px;
    top: 284px;
    margin: 0;
    text-align: center;
    font-family: "Oswald", sans-serif;
    font-weight: 200;
    font-size: 13px;
    letter-spacing: 0.5px;
    color: var(--ink-soft);
  }

  .back-label {
    position: absolute;
    left: 0;
    top: 0;
    width: 210px;
    height: 466px;
    font-family: "Bodoni Moda", serif;
    color: var(--ink);
  }
  .unisex-mark {
    position: absolute;
    left: 96px;
    top: 177px;
    width: 14px;
    height: 14px;
    border-radius: 50%;
    border: 2px solid var(--ink);
    box-sizing: border-box;
  }
  .ingredients {
    position: absolute;
    left: 48px;
    width: 112px;
    top: 204px;
    margin: 0;
    text-align: center;
    font-size: 5.6px;
    line-height: 8.4px;
    text-transform: uppercase;
    word-break: break-all;
  }
  .certification {
    position: absolute;
    left: 0;
    width: 206px;
    top: 306px;
    margin: 0;
    text-align: center;
    font-size: 6.5px;
    text-transform: uppercase;
  }
  .back-dot {
    position: absolute;
    left: 93px;
    top: 394px;
    width: 20px;
    height: 20px;
    border-radius: 50%;
    border: 1px solid var(--ink-soft);
    box-sizing: border-box;
  }
</style>
</head>
<body>
<main class="canvas">

  <section class="tube tube--front" aria-label="Tube front label">
    <div class="tube__crimp"></div>
    <div class="tube__body">
      <div class="front-label">
        <h1 class="brand-name">Fjellmark<br>Botanics</h1>
        <h2 class="product-name">Charcoal Activated<br>Face Mask</h2>
        <p class="tagline">restores your youthful glow</p>
        <span class="brand-dot" aria-hidden="true"></span>
        <p class="volume">330ML</p>
      </div>
    </div>
    <div class="tube__cap"></div>
  </section>

  <section class="tube tube--back" aria-label="Tube back label">
    <div class="tube__crimp"></div>
    <div class="tube__body">
      <div class="back-label">
        <span class="unisex-mark" aria-hidden="true"></span>
        <p class="ingredients">Ingredients:water,polyvinyl alcohol,alcohol,aluminum chlorohydrate,bamboo charcoal,zea mays(corn) starch,peg-40 hydrogenated castor oil,methylisothiazolinone,iodopropynyl butylcarbamate</p>
        <p class="certification">ISO901 &amp; GMPC Certified</p>
        <span class="back-dot" aria-hidden="true"></span>
      </div>
    </div>
    <div class="tube__cap"></div>
  </section>

</main>
</body>
</html>
```